Business Card Design

Velvet Pixel Promotions

An online marketing consulting & strategy business for the cosmetic niche

We specialise in Increasing Leads, Conversions & Content Marketing

I am looking for a very clean, BOLD business card that is simple & effective

Target Market(s)

cosmetic surgeons & cosmetic clinics

Industry/Entity Type

Marketing

Contact Information for Business Card

Darren Okoye
Online Marketing Strategist

Darren@VelvetPixelPromotions.example
0491 268 517

LinkedIn: in/darrenokoye

```html
<!DOCTYPE html>
<html lang="en">
<head>
<meta charset="utf-8">
<title>Velvet Pixel Promotions — Business Card</title>
<link href="https://fonts.googleapis.com/css2?family=Open+Sans:wght@400;600;700&display=swap" rel="stylesheet">
<style>
  :root{
    --stage:#8c8c8c;
    --teal:#00b3e0;
    --mint:#1ebc9c;
    --lime:#86c540;
    --ink:#1a1a1a;
    --slate:#5f6063;
    --sky:#1aa6e4;
    --paper:#ffffff;
  }
  *{margin:0;padding:0;box-sizing:border-box}
  html,body{width:1200px;height:900px;overflow:hidden}
  body{
    background:var(--stage);
    font-family:"Open Sans",Arial,sans-serif;
    position:relative;
  }
  .card{
    position:absolute;
    width:560px;height:320px;
    overflow:hidden;
    box-shadow:0 10px 26px rgba(0,0,0,.35);
  }
  /* Front side */
  .card--front{
    left:90px;top:100px;
    background:linear-gradient(180deg,var(--teal) 0%,var(--mint) 50%,var(--lime) 100%);
  }
  .front__mark{
    position:absolute;left:40px;top:50px;
    width:220px;height:220px;border-radius:50%;
    background:rgba(255,255,255,.16);
  }
  .wordmark{
    text-transform:uppercase;
    font-weight:600;
    letter-spacing:.14em;
    line-height:1.1;
    white-space:nowrap;
  }
  .front__wordmark{
    position:absolute;left:295px;top:112px;
    color:var(--paper);
    font-size:26px;
  }
  /* Back side */
  .card--back{
    left:550px;top:480px;
    background:var(--paper);
  }
  .back__wordmark{
    position:absolute;right:36px;top:30px;
    color:var(--slate);
    font-size:26px;
  }
  .back__mark{
    position:absolute;left:34px;top:130px;
    width:150px;height:150px;border-radius:50%;
    background:linear-gradient(180deg,var(--sky),var(--lime));
  }
  .contact{
    position:absolute;left:210px;top:150px;
    color:var(--ink);
  }
  .contact__name{
    color:var(--sky);
    font-weight:700;
    font-size:17px;
    text-transform:uppercase;
    letter-spacing:.02em;
  }
  .contact__role{font-size:12px;margin-top:2px}
  .contact__list{list-style:none;margin-top:22px}
  .contact__item{
    display:flex;align-items:center;gap:9px;
    font-size:12.5px;line-height:22px;
  }
  .contact__icon{width:12px;height:12px;flex:none}
</style>
</head>
<body>

  <section class="card card--front" aria-label="Card front">
    <div class="front__mark"></div>
    <p class="wordmark front__wordmark">Velvet<br>Pixel<br>Promotions</p>
  </section>

  <section class="card card--back" aria-label="Card back">
    <p class="wordmark back__wordmark">Velvet<br>Pixel<br>Promotions</p>
    <div class="back__mark"></div>
    <div class="contact">
      <h1 class="contact__name">Darren Okoye</h1>
      <p class="contact__role">Online Marketing Strategist</p>
      <ul class="contact__list">
        <li class="contact__item">
          <svg class="contact__icon" viewBox="0 0 12 12"><rect width="12" height="12" rx="3" fill="#1aa6e4"/><rect x="4" y="2.5" width="4" height="7" rx="1" fill="none" stroke="#fff" stroke-width="1"/></svg>
          0491 268 517
        </li>
        <li class="contact__item">
          <svg class="contact__icon" viewBox="0 0 12 12"><rect width="12" height="12" rx="3" fill="#1aa6e4"/><rect x="2.5" y="3.5" width="7" height="5" fill="none" stroke="#fff" stroke-width="1"/><path d="M2.5 3.5 6 6.3 9.5 3.5" fill="none" stroke="#fff" stroke-width="1"/></svg>
          Darren@VelvetPixelPromotions.example
        </li>
        <li class="contact__item">
          <svg class="contact__icon" viewBox="0 0 12 12"><rect width="12" height="12" rx="3" fill="#1aa6e4"/></svg>
          in/darrenokoye
        </li>
      </ul>
    </div>
  </section>

</body>
</html>
```